FotoVELTA buisnesscard

Hey :) I need a modern buisnesscard for my company FotoVELTA
It most have:
Dagligleder og Fotograf: Henrik Torvald Bjelland

Mob: +4791642058
Epost: post@fotovelta.no
Adresse: Bakkestien22, 5412 Fjellvik

Facbook and instagram logo with text FotoVELTA

FotoVELTA logo

It Company

```html
<!DOCTYPE html>
<html lang="no">
<head>
<meta charset="utf-8">
<title>FotoVELTA – visittkort</title>
<link rel="stylesheet" href="https://fonts.googleapis.com/css2?family=Exo+2:wght@300;600&display=swap">
<style>
  :root {
    --page-bg: #e4e4e4;
    --card-dark: #161616;
    --card-mid: #3a3a3a;
    --panel-left: #252525;
    --footer-strip: #1c1c1c;
    --rule: #b9b9b9;
    --text-light: #c9c9c9;
    --text-soft: #a9a9a9;
  }
  * { margin: 0; padding: 0; box-sizing: border-box; }
  html, body {
    width: 1200px; height: 1200px; overflow: hidden;
    background: var(--page-bg);
    font-family: "Exo 2", sans-serif;
  }
  .card {
    position: absolute; left: 315px; width: 570px;
    box-shadow: 0 10px 18px rgba(0,0,0,0.28);
  }
  /* front side */
  .card--front {
    top: 238px; height: 343px;
    background: radial-gradient(ellipse at 50% 40%, var(--card-mid) 0%, var(--card-dark) 75%);
  }
  .front-rule {
    position: absolute; top: 206px; height: 4px; background: var(--rule);
  }
  .front-rule--left { left: 0; width: 179px; }
  .front-rule--right { left: 396px; right: 0; }
  .brand-name {
    position: absolute; top: 188px; left: 0; width: 100%;
    text-align: center; font-weight: 600; font-size: 29px; line-height: 40px;
    color: var(--rule); letter-spacing: 0.5px;
  }
  /* back side */
  .card--back {
    top: 671px; height: 351px;
    background: var(--footer-strip);
  }
  .back-panels { position: absolute; inset: 0; }
  .back-brand {
    position: absolute; left: 62px; top: 94px;
    font-weight: 600; font-size: 22px; line-height: 30px; color: var(--rule);
  }
  .holder-name {
    position: absolute; left: 319px; top: 142px;
    font-weight: 300; font-size: 19px; line-height: 24px; color: var(--text-light);
  }
  .notch {
    position: absolute; right: 0; top: 144px;
    width: 0; height: 0;
    border-top: 10px solid transparent; border-bottom: 10px solid transparent;
    border-right: 12px solid var(--page-bg);
  }
  .contact-list { list-style: none; position: absolute; left: 300px; top: 184px; }
  .contact-item {
    display: flex; align-items: center; height: 35.5px;
    font-weight: 300; font-size: 15px; color: var(--text-soft);
    white-space: nowrap;
  }
  .contact-icon { width: 10px; height: 12px; margin-right: 10px; fill: var(--text-soft); }
  .social {
    position: absolute; top: 326px; left: 82px; right: 0;
    display: flex; justify-content: center; align-items: center;
    font-weight: 300; font-size: 14px; line-height: 18px; color: var(--text-soft);
  }
  .social-mark { width: 9px; height: 9px; background: var(--text-soft); margin-right: 8px; }
</style>
</head>
<body>
  <section class="card card--front">
    <div class="front-rule front-rule--left"></div>
    <div class="front-rule front-rule--right"></div>
    <div class="brand-name">FotoVELTA</div>
  </section>

  <section class="card card--back">
    <svg class="back-panels" width="570" height="351" viewBox="0 0 570 351">
      <defs>
        <linearGradient id="rightPanel" x1="0" y1="0" x2="1" y2="1">
          <stop offset="0" stop-color="#353535"/>
          <stop offset="1" stop-color="#262626"/>
        </linearGradient>
        <linearGradient id="foldShade" x1="0" y1="0" x2="1" y2="0">
          <stop offset="0" stop-color="#000" stop-opacity="0.55"/>
          <stop offset="1" stop-color="#000" stop-opacity="0"/>
        </linearGradient>
      </defs>
      <rect x="0" y="0" width="570" height="316" fill="var(--panel-left)"/>
      <polygon points="391,0 570,0 570,316 82,316" fill="url(#rightPanel)"/>
      <polygon points="391,0 402,0 100,316 82,316" fill="url(#foldShade)"/>
      <polygon points="0,316 82,316 30,351 0,351" fill="#121212"/>
      <rect x="82" y="314" width="488" height="4" fill="var(--rule)"/>
    </svg>

    <div class="back-brand">FotoVELTA</div>
    <div class="holder-name">Henrik Torvald Bjelland</div>
    <div class="notch"></div>

    <ul class="contact-list">
      <li class="contact-item">
        <svg class="contact-icon" viewBox="0 0 10 12"><rect x="2" y="0" width="6" height="12" rx="1"/></svg>
        +4791642058
      </li>
      <li class="contact-item">
        <svg class="contact-icon" viewBox="0 0 10 12"><rect x="0" y="3" width="10" height="7"/></svg>
        post@fotovelta.no
      </li>
      <li class="contact-item">
        <svg class="contact-icon" viewBox="0 0 10 12"><path d="M5 0a4 4 0 0 1 4 4c0 3-4 8-4 8S1 7 1 4a4 4 0 0 1 4-4zm0 2.5a1.5 1.5 0 1 0 0 3 1.5 1.5 0 0 0 0-3z"/></svg>
        Bakkestien22, 5412 Fjellvik
      </li>
    </ul>

    <div class="social"><span class="social-mark"></span>FotoVELTA</div>
  </section>
</body>
</html>
```